ultra-minimalist business card

front (black background, matte):

tarik b. hosseny
writer | photographer
get@tarikhosseny.com

back (white background, matte):

a picture speaks a thousand words;
a word draws a thousand pictures.

www.tarikhosseny.com

all text should be small (white or silver - as long as it shows against the black - on the front; black or gray - as long as it shows against the white - on the back).

feel free to get creative in terms of arrangement, alignment, and font type, but remember, the overall style is minimalist, so nothing too fancy, please.

thanks.

```html
<!DOCTYPE html>
<html lang="en">
<head>
<meta charset="utf-8">
<title>tarik b. hosseny — business card</title>
<link rel="stylesheet" href="https://fonts.googleapis.com/css2?family=Didact+Gothic&family=Dancing+Script:wght@400&display=swap">
<style>
  :root {
    --ink: #000000;
    --paper: #ffffff;
    --paper-tint: #f6f6f6;
    --silver: #d9d6d6;
    --text-light: #ffffff;
    --text-dark: #111111;
  }
  * { margin: 0; padding: 0; box-sizing: border-box; }
  html, body {
    width: 1200px;
    height: 1200px;
    overflow: hidden;
    background: var(--paper);
  }
  .sheet {
    position: relative;
    width: 1200px;
    height: 1200px;
  }
  .card {
    position: absolute;
    left: 90px;
    width: 1020px;
  }
  .card--front {
    top: 8px;
    height: 586px;
    background: var(--ink);
    border-bottom: 2px solid var(--paper);
    box-shadow: 0 3px 0 var(--ink);
  }
  .card--back {
    top: 602px;
    height: 584px;
    background: var(--paper-tint);
    border: 3px solid var(--ink);
  }
  .texture {
    position: absolute;
    inset: 0;
    background: var(--paper-tint);
  }
  .divider {
    position: absolute;
    left: 509px;
    top: 56px;
    width: 2px;
    height: 472px;
    background: linear-gradient(to bottom, rgba(217,214,214,0), var(--silver) 50%, rgba(217,214,214,0));
  }
  .rule {
    position: absolute;
    left: 58px;
    width: 404px;
    height: 2px;
    background: linear-gradient(to right, rgba(217,214,214,0), var(--silver) 50%, rgba(217,214,214,0));
  }
  .rule--top { top: 254px; }
  .rule--bottom { top: 332px; }
  .email {
    position: absolute;
    left: 58px;
    width: 404px;
    top: 277px;
    text-align: center;
    font-family: "Didact Gothic", "Century Gothic", sans-serif;
    font-size: 29px;
    line-height: 1;
    color: var(--text-light);
  }
  .identity {
    position: absolute;
    left: 560px;
    width: 400px;
    top: 220px;
    text-align: center;
    color: var(--text-light);
  }
  .identity__name {
    font-family: "Dancing Script", cursive;
    font-size: 44px;
    line-height: 1;
    letter-spacing: 1px;
  }
  .identity__role {
    margin-top: 10px;
    font-family: "Didact Gothic", "Century Gothic", sans-serif;
    font-size: 29px;
    line-height: 1;
  }
  .motto {
    position: absolute;
    left: 0;
    right: 0;
    top: 182px;
    text-align: center;
    font-family: "Didact Gothic", "Century Gothic", sans-serif;
    font-style: italic;
    font-size: 36px;
    line-height: 45px;
    color: var(--text-dark);
  }
  .website {
    position: absolute;
    left: 284px;
    top: 405px;
    width: 446px;
    height: 72px;
    background: var(--ink);
    color: var(--text-light);
    font-family: "Didact Gothic", "Century Gothic", sans-serif;
    font-size: 29px;
    line-height: 72px;
    text-align: center;
  }
</style>
</head>
<body>
<main class="sheet">
  <section class="card card--front">
    <div class="divider"></div>
    <div class="rule rule--top"></div>
    <p class="email">get@tarikhosseny.com</p>
    <div class="rule rule--bottom"></div>
    <div class="identity">
      <p class="identity__name">tarik b. hosseny</p>
      <p class="identity__role">writer&nbsp; | &nbsp;photographer</p>
    </div>
  </section>

  <section class="card card--back">
    <div class="texture" role="img" aria-label="faint light grey swirl pattern background"></div>
    <p class="motto">a picture speaks a thousand words;<br>a word draws a thousand pictures.</p>
    <p class="website">www.tarikhosseny.com</p>
  </section>
</main>
</body>
</html>
```